Classy business card for accounting firm

We're looking for a new business card for our accounting firm. Our logo was designed by Brandolith, so all of the design info we would like to use has been provided. The specific font provided isn't required to be used.

We want the card to look classy and elegent. Probably more minimalistic, but still with some pops of color.

The options we would like to include on the card are as follows:
1. Main office phone line
2. Direct phone line
3. Email address
4. Website URL
5. Name
6. Title (CEO, President, etc.)
7. Firm Address

The design and card should be double sided!!! The drop down box in the project brief for some reason is defaulting to single sided. Not sure why this is happening.

Thanks!

Contact Information for Business Card

The options we would like to include on the card are as follows: 1. Main office phone line 2. Direct phone line 3. Email address 4. Website URL 5. Name 6. Title (CEO, President, etc.) 7. Firm Address

Requirements
Must have
• Card must be double sided.

```html
<!DOCTYPE html>
<html lang="en">
<head>
<meta charset="utf-8">
<title>Ledgerline Associates – Business Card</title>
<link href="https://fonts.googleapis.com/css2?family=Montserrat:wght@400;500;600;700&display=swap" rel="stylesheet">
<style>
  :root {
    --backdrop: #3b3b3b;
    --card: #151515;
    --lime: #a8c232;
    --orange: #f07a1c;
    --white: #f2f2f2;
    --muted: #5a5a5a;
  }
  * { box-sizing: border-box; margin: 0; padding: 0; }
  html, body { width: 1200px; height: 801px; overflow: hidden; }
  body {
    background: var(--backdrop);
    font-family: "Montserrat", Arial, sans-serif;
    position: relative;
  }
  .card {
    position: absolute;
    width: 525px;
    height: 300px;
    background: var(--card);
    border: 2px solid var(--lime);
    top: 250px;
  }
  .card--front { left: 50px; }
  .card--back { left: 625px; }

  /* Front header */
  .brand {
    position: absolute;
    left: 44px;
    top: 54px;
    display: flex;
    align-items: center;
    gap: 16px;
  }
  .brand__mark {
    width: 40px; height: 40px;
    background: var(--orange);
  }
  .brand__name {
    color: var(--white);
    font-size: 27px;
    font-weight: 500;
    letter-spacing: 2.5px;
    line-height: 1;
  }
  .tagline {
    display: flex;
    align-items: center;
    gap: 10px;
    margin-top: 6px;
  }
  .tagline__rule { height: 1px; background: var(--lime); flex: 1; }
  .tagline__text {
    color: var(--white);
    font-size: 10px;
    font-weight: 600;
    letter-spacing: 2px;
    white-space: nowrap;
  }

  /* Front body */
  .details {
    position: absolute;
    left: 44px;
    right: 30px;
    top: 150px;
    display: flex;
  }
  .person { width: 215px; padding-top: 4px; }
  .person__name {
    color: var(--lime);
    font-size: 20px;
    font-weight: 700;
    letter-spacing: 0.5px;
  }
  .person__title {
    color: var(--orange);
    font-size: 13px;
    font-weight: 500;
    text-align: right;
    margin-top: -2px;
    margin-right: 20px;
  }
  .person__address {
    color: var(--white);
    font-size: 13px;
    line-height: 1.45;
    margin-top: 14px;
  }
  .divider { width: 1px; background: var(--lime); height: 78px; margin: 0 18px 0 4px; }
  .contacts { list-style: none; }
  .contacts li {
    color: var(--white);
    font-size: 13px;
    display: flex;
    align-items: center;
    gap: 8px;
    line-height: 1.55;
  }
  .contacts svg { width: 11px; height: 11px; flex: none; }

  /* Back */
  .back-name {
    position: absolute;
    inset: 0;
    display: flex;
    align-items: center;
    justify-content: center;
    color: var(--muted);
    font-size: 30px;
    font-weight: 600;
    letter-spacing: 4px;
  }
</style>
</head>
<body>

<section class="card card--front">
  <header class="brand">
    <div class="brand__mark"></div>
    <div>
      <div class="brand__name">LEDGERLINE ASSOCIATES</div>
      <div class="tagline">
        <span class="tagline__rule"></span>
        <span class="tagline__text">SOLVING TAX PROBLEMS</span>
        <span class="tagline__rule"></span>
      </div>
    </div>
  </header>

  <div class="details">
    <div class="person">
      <div class="person__name">MARCUS BELLAMY</div>
      <div class="person__title">President</div>
      <p class="person__address">1187 Harbor Crest Way<br>Seabrook Bay CA 90417</p>
    </div>
    <div class="divider"></div>
    <ul class="contacts">
      <li>
        <svg viewBox="0 0 12 12"><rect x="3" y="0.5" width="6" height="11" rx="1" fill="none" stroke="var(--lime)" stroke-width="1.3"/></svg>
        555-210-4837
      </li>
      <li>
        <svg viewBox="0 0 12 12"><path d="M2 1 L4.5 1 L5.5 4 L4 5 C4.8 6.8 5.2 7.2 7 8 L8 6.5 L11 7.5 L11 10 C6 11 1 6 2 1 Z" fill="var(--lime)"/></svg>
        555-210-4838
      </li>
      <li>
        <svg viewBox="0 0 12 12"><rect x="0.5" y="2.5" width="11" height="7" fill="var(--lime)"/><path d="M0.5 2.5 L6 7 L11.5 2.5" fill="none" stroke="var(--card)" stroke-width="1"/></svg>
        info@LedgerlineAssociates.com
      </li>
      <li>
        <svg viewBox="0 0 12 12"><circle cx="6" cy="6" r="5.2" fill="var(--lime)"/><path d="M1 6 H11 M6 1 C3.5 4 3.5 8 6 11 M6 1 C8.5 4 8.5 8 6 11" fill="none" stroke="var(--card)" stroke-width="0.8"/></svg>
        www.LedgerlineAssociates.com
      </li>
    </ul>
  </div>
</section>

<section class="card card--back">
  <div class="back-name">LEDGERLINE</div>
</section>

</body>
</html>
```